Business card for a boutique travel agency VELARIEN

we need a business card design - double sided. We would like to have a very elegant, sophisticated but modern design. we are travel consultants and our business focus is Europe, mainly the city of Paris. We would like to receive designs in white and silver, black color but if you are confident that we should pick up a color to make it different and more beautful...go ahead! We are going to give business cards to our clients and business partners. It is important to be perceived as elegant, modern and trustful. Please check jpg references.

Target Market(s)

Velarien primary clients are individuals, couples and affinity groups of high-net-worth who travel for leisure at least once per year. Seeking the ultimate travel experience, the target clients demand the finest quality activities and accommodations accompanied by a superior level of service.

Industry/Entity Type

Travel Industry

Contact Information for Business Card

Lucinda Farrow
- lucinda@velarien-example.com
- +55 11 98347.2516
- velarien-example.com
- unique travel experiences (we would like to see this signature printed as a detail)

Font styles to use
Sans Serif

Colors

Designer to choose colors to be used in the design.

Requirements
Must have
• the Velarien logo that I have attached
Nice to have
• we would like to have some nice detail, something different that shows that we care about,... we are detail oriented.
Should not have
• decorative fonts

```html
<!DOCTYPE html>
<html lang="en">
<head>
<meta charset="utf-8">
<title>Velarien — Business Card</title>
<link href="https://fonts.googleapis.com/css2?family=Josefin+Sans:wght@300;400&display=swap" rel="stylesheet">
<style>
  :root {
    --backdrop: #141414;
    --card-white: #ffffff;
    --band-silver: #e8e8ea;
    --pattern-tone: #f1f1f2;
    --ink: #1c1c1c;
    --ink-soft: #3a3a3a;
  }
  * { margin: 0; padding: 0; box-sizing: border-box; }
  html, body {
    width: 1200px; height: 1000px; overflow: hidden;
    background: var(--backdrop);
    font-family: "Josefin Sans", Arial, sans-serif;
    color: var(--ink);
  }
  .stage { position: relative; width: 1200px; height: 1000px; }
  .card {
    position: absolute; top: 350px;
    width: 520px; height: 300px;
    background: var(--card-white);
    overflow: hidden;
  }
  .card--front { left: 50px; }
  .card--back { left: 630px; }

  /* Front */
  .front-mark {
    position: absolute; inset: 0;
    display: flex; align-items: center; justify-content: center; gap: 18px;
  }
  .front-mark__dot {
    width: 14px; height: 14px; border-radius: 50%;
    background: var(--band-silver);
  }
  .front-mark__name {
    font-weight: 300; font-size: 30px; letter-spacing: 14px;
    color: var(--ink);
  }

  /* Back */
  .back-pattern {
    position: absolute; left: 0; top: 0; width: 100%; height: 120px;
    background: var(--pattern-tone);
  }
  .back-band {
    position: absolute; left: 0; top: 120px; width: 100%; height: 180px;
    background: var(--band-silver);
  }
  .back-brand {
    position: absolute; right: 30px; top: 78px; text-align: right;
  }
  .back-brand__name {
    font-weight: 300; font-size: 26px; letter-spacing: 10px; margin-right: -10px;
    line-height: 1;
  }
  .back-brand__tagline {
    font-weight: 300; font-size: 17px; letter-spacing: 1px; margin-top: 4px;
  }
  .back-contact {
    position: absolute; left: 32px; top: 150px;
  }
  .back-contact__name {
    font-weight: 400; font-size: 20px; letter-spacing: 1px; text-transform: uppercase;
    margin-bottom: 14px;
  }
  .back-contact__line {
    font-weight: 300; font-size: 13px; color: var(--ink-soft); line-height: 1.6;
  }
</style>
</head>
<body>
<main class="stage">
  <section class="card card--front" aria-label="Card front">
    <div class="front-mark">
      <span class="front-mark__dot"></span>
      <span class="front-mark__name">VELARIEN</span>
    </div>
  </section>

  <section class="card card--back" aria-label="Card back">
    <div class="back-pattern" role="img" aria-label="Fine repeating pattern of small circles in pale silver"></div>
    <div class="back-band"></div>
    <div class="back-brand">
      <div class="back-brand__name">VELARIEN</div>
      <div class="back-brand__tagline">unique travel experiences</div>
    </div>
    <div class="back-contact">
      <div class="back-contact__name">Lucinda Farrow</div>
      <div class="back-contact__line">+55 11 98347.2516</div>
      <div class="back-contact__line">lucinda@velarien-example.com &nbsp;|&nbsp; www.velarien-example.com</div>
    </div>
  </section>
</main>
</body>
</html>
```